Website Landing Page for Brightfall Systems

Create a custom designed website landing page for our business. Looking for a professional upscale design that incorporates our logo and logo colors into the theme. I want a standard fixed frame website, not a constant scrolling format that seems to be the trend. To start with I'm looking for more of the graphic design part, maybe a concept or theme, I don't expect to see a finished project. Not interested in generic templates or layouts.

The name of our company is Brightfall Systems and I've attached our logo below. I'd like to have the web page have the same look and feel of our logo, as well as the colors. Our company, Brightfall Systems does system design, installation, and programming, of residential and commercial Audio/Video and Automation systems. We do home theaters, lighting and building automation, video conferencing systems, security camera installations, conference rooms, projectors, distributed audio systems, and similar Technology projects. This will be a professional services/informational website. We will not sell products on this website. This website will be used to advertise our company and communicate our services to prospective customers. Having a well designed, professional and clean website is one way we want to distinguish our company from the competition.

Here are some examples of what I consider a professional well designed website
http://www.qorlamstudio.com/Work/

Last year we had our tradlo store designed (with PixelMarket) and I'm really happy with the way it turned out. You can see it at www.HolvenGearDepot.com I consider this to be a great design and looking for the same level of quality with this new website. However, do not copy or use any part of this design in this new project. This tradlo store is completely separate from our other company Brightfall Systems. I only mention this tradlo store an an example of good work.

Reason: Still going through designs.

Reason: Still working on project and have not had time to review all designs and request revisions.

Reason: Sill going through designs and requesting revisions

Reason: still going through all the submissions we received.

Target Market(s)

People interested in Audio/Video, home theaters, home automation. We do sales, system design, and programming. We typically work on larger projects with both residential and commercial customers.

Industry/Entity Type

Business

Number of Pages Required

1 page

Requirements
Must have
• Great design elements. Please use a white background. I think white goes well with our logo colors.

```html
<!DOCTYPE html>
<html lang="en">
<head>
<meta charset="utf-8">
<title>Brightfall Systems</title>
<link href="https://fonts.googleapis.com/css2?family=Roboto+Condensed:ital,wght@0,300;0,400;0,700;1,300;1,400&family=Roboto:ital,wght@0,300;0,400;0,500;0,700;1,300;1,400&display=swap" rel="stylesheet">
<style>
:root{
  --green:#6cbf45;
  --green-dark:#57a935;
  --blue:#2b84c6;
  --ink:#333a40;
  --muted:#6d7378;
  --soft:#9aa0a5;
  --panel:#f1f1f1;
  --footer:#3d3f41;
  --night:#121212;
  --white:#ffffff;
}
*{box-sizing:border-box;margin:0;padding:0}
html,body{width:1200px;height:4119px;overflow:hidden}
body{position:relative;background:var(--white);font-family:"Roboto",Arial,sans-serif;color:var(--ink)}
.abs{position:absolute}

/* hero */
.hero{left:0;top:0;width:1200px;height:675px;overflow:hidden}
.hero-photo{left:0;top:0;width:1200px;height:675px;background:linear-gradient(180deg,#c9d6e2 0%,#dde5ec 35%,#c2c8cc 62%,#9aa39f 100%)}
.hero-cut{left:0;top:0;width:1200px;height:675px}
.brand{left:128px;top:24px;display:flex;align-items:center;gap:12px}
.brand-dot{width:56px;height:56px;border-radius:50%;border:5px solid var(--green)}
.brand-name{font-family:"Roboto Condensed",sans-serif;font-weight:700;font-size:22px;line-height:24px;color:var(--blue);width:170px;text-transform:uppercase}
.nav{right:128px;top:44px;display:flex;gap:46px;font-family:"Roboto Condensed",sans-serif;font-size:17px;color:var(--ink)}
.nav .active{color:var(--green)}
.hero-title{left:0;top:262px;width:1200px;text-align:center;font-family:"Roboto Condensed",sans-serif;font-weight:700;font-size:34px;color:var(--green);text-transform:uppercase}
.hero-sub{left:400px;top:318px;width:400px;text-align:center;font-style:italic;font-size:15px;line-height:22px;color:var(--ink)}
.scroll-ring{left:583px;top:598px;width:34px;height:46px}

/* intro */
.intro-kicker{left:128px;top:745px;font-family:"Roboto Condensed",sans-serif;font-weight:300;font-size:44px;color:var(--blue);text-transform:uppercase}
.intro-title{left:128px;top:795px;font-family:"Roboto Condensed",sans-serif;font-size:44px;color:var(--blue);text-transform:uppercase}
.intro-text{left:128px;top:868px;width:520px;font-size:15px;line-height:27px;color:var(--muted)}
.product-photo{left:820px;top:705px;width:250px;height:350px;background:linear-gradient(180deg,#f4f5f6 0%,#e6e8ea 55%,#f7f7f8 100%)}

/* features */
.section-title{left:0;width:1200px;text-align:center;font-family:"Roboto Condensed",sans-serif;font-weight:700;font-size:26px;text-transform:uppercase}
.section-lead{left:330px;width:540px;text-align:center;font-style:italic;font-size:13px;line-height:21px;color:var(--muted)}
.feature{width:280px;text-align:center}
.feature svg{display:block;margin:0 auto 10px}
.feature h3{font-family:"Roboto Condensed",sans-serif;font-weight:700;font-size:16px;color:#4a5055;text-transform:uppercase;margin-bottom:10px}
.feature p{font-style:italic;font-size:12px;line-height:20px;color:var(--soft)}

/* banner */
.banner{left:0;top:1587px;width:1200px;height:508px;background:linear-gradient(180deg,#7fc459 0%,#6dbd48 45%,#62b63e 100%)}
.banner-title{left:0;top:1752px;width:1200px;text-align:center;font-family:"Roboto Condensed",sans-serif;font-weight:700;font-size:34px;color:var(--white);text-transform:uppercase}
.banner-title span{color:#111}
.banner-text{left:200px;top:1808px;width:800px;text-align:center;font-size:15px;color:var(--white)}
.btn{display:flex;align-items:center;justify-content:center;border-radius:26px;font-family:"Roboto Condensed",sans-serif;font-weight:700;font-size:14px;text-transform:uppercase}
.btn-outline{left:442px;top:1874px;width:148px;height:50px;border:2px solid var(--white);color:var(--white)}
.btn-solid{left:612px;top:1874px;width:148px;height:50px;background:var(--white);color:var(--green-dark)}

/* gallery */
.tile{top:2353px;width:228px;height:277px}
.tile-label{left:0;bottom:0;width:100%;height:42px;background:rgba(20,20,20,.85);color:var(--white);display:flex;align-items:center;justify-content:space-between;padding:0 10px;font-family:"Roboto Condensed",sans-serif;font-size:13px;text-transform:uppercase}

/* pricing */
.pricing{left:0;top:2732px;width:1200px;height:604px;background:var(--panel)}
.plan{top:2848px;width:296px;height:425px;background:var(--white);border-radius:6px;text-align:center}
.plan-ring{position:absolute;left:95px;top:40px;width:106px;height:106px;border:2px solid var(--green);border-radius:50%;padding-top:20px}
.plan-ring small{display:block;font-size:11px;color:var(--soft);text-transform:uppercase}
.plan-ring b{display:block;font-family:"Roboto Condensed",sans-serif;font-size:26px;color:var(--green-dark);line-height:32px}
.plan-ring em{display:block;font-style:normal;font-size:11px;color:var(--muted)}
.plan p{position:absolute;left:50px;top:190px;width:196px;font-style:italic;font-size:12px;line-height:22px;color:var(--muted)}
.plan .btn{position:absolute;left:100px;top:340px;width:96px;height:42px;background:var(--green);color:var(--white);font-size:12px;font-weight:400}

/* partners */
.partners{left:129px;top:3455px;width:942px;display:flex;justify-content:space-between;align-items:center;font-family:"Roboto Condensed",sans-serif;font-weight:700;font-size:30px;color:#c3c6c8;text-transform:uppercase}

/* footer */
.footer{left:0;top:3589px;width:1200px;height:530px;background:var(--footer)}
.contact-card{left:129px;top:3671px;width:310px;height:297px;background:var(--white);padding:42px 22px}
.contact-card h4{font-family:"Roboto Condensed",sans-serif;font-size:12px;color:var(--green-dark);text-transform:uppercase;margin-bottom:10px}
.contact-card p{font-size:10px;line-height:14px;color:var(--ink)}
.contact-card .row{margin-top:12px}
.contact-card .row h5{display:flex;align-items:center;gap:5px;font-size:10px;color:var(--green-dark);text-transform:uppercase;margin-bottom:3px}
.map{left:439px;top:3671px;width:316px;height:297px;background:linear-gradient(160deg,#eceae6,#dcdad6)}
.comment{left:774px;top:3671px;width:297px;height:297px;background:var(--night);padding:40px 20px}
.comment h4{font-family:"Roboto Condensed",sans-serif;font-size:16px;color:var(--white);text-transform:uppercase;margin-bottom:22px}
.field{border:1px solid #6a6a6a;height:32px;margin-bottom:10px;font-size:9px;color:#bbb;padding:10px 8px}
.field.tall{height:80px}
.comment .btn{width:96px;height:32px;margin:12px auto 0;background:var(--green);color:var(--white);font-size:11px}
.copyright{left:0;top:4072px;width:1200px;text-align:center;font-size:10px;color:#9b9d9f}
</style>
</head>
<body>

<section class="hero abs">
  <div class="hero-photo abs" role="img" aria-label="City skyline photograph under a pale cloudy sky"></div>
  <svg class="hero-cut abs" viewBox="0 0 1200 675" aria-hidden="true"><polygon points="0,480 600,672 1200,480 1200,675 0,675" fill="#ffffff"/></svg>
  <div class="brand abs"><span class="brand-dot"></span><span class="brand-name">Brightfall Systems</span></div>
  <nav class="nav abs"><span class="active">Home</span><span>About us</span><span>Download</span><span>Pricing</span><span>Blog</span><span>Contact</span></nav>
  <h1 class="hero-title abs">Cras tempor tortor venenatis vulputate</h1>
  <p class="hero-sub abs">Suspendisse potenti. Vestibulum diam erat, finibus eget arcu sed, interdum venenatis ligula. Nulla posuere orci facilisis elit posuere elementum.</p>
  <svg class="scroll-ring abs" viewBox="0 0 34 46" aria-hidden="true"><rect x="2" y="2" width="30" height="42" rx="15" fill="none" stroke="#8a8f93" stroke-width="2"/><path d="M13 22l4 5 4-5" fill="none" stroke="#8a8f93" stroke-width="2"/></svg>
</section>

<h2 class="intro-kicker abs">Consectetur</h2>
<h2 class="intro-title abs">Etiam venenatis lacus</h2>
<p class="intro-text abs">Non porttitor. Morbi nec dolor vehicula, suscipit lorem et, finibus elit. Suspendisse a tristique lorem. Maecenas vel quam sapien. Praesent consequat ut tellus ultrices tristique. Donec convallis ullamcorper rhoncus. Nullam maxima ididictum commodo nunc.</p>
<div class="product-photo abs" role="img" aria-label="Product photo of a white home security camera"></div>

<h2 class="section-title abs" style="top:1150px;color:var(--blue)">Nunc sem neque cras ante ante</h2>
<p class="section-lead abs" style="top:1200px">Tincidunt nec blandit quis, porttitor sed urna. In volutpat ultrices pharetra. Nunc a lobortis ligula. Ut id felis erat. Suspendisse potenti. Nulla dapibus a lectus id porttitor. Nam cursus lectus.</p>

<div class="feature abs" style="left:130px;top:1310px">
  <svg width="60" height="60" viewBox="0 0 60 60" aria-hidden="true"><circle cx="30" cy="30" r="24" fill="none" stroke="#6cbf45" stroke-width="3"/><path d="M18 22c2 10 10 18 20 20l4-5-6-4-3 3c-4-2-7-5-9-9l3-3-4-6z" fill="#6cbf45"/></svg>
  <h3>Nullam vulputate</h3>
  <p>Tellus eget nisl tincidunt fermentum. Aliquam ac ante quis lorem mattis rutrum at ut sem. Vivamus diam orci, condimentum.</p>
</div>
<div class="feature abs" style="left:460px;top:1310px">
  <svg width="60" height="60" viewBox="0 0 60 60" aria-hidden="true"><rect x="20" y="16" width="20" height="34" rx="3" fill="none" stroke="#6cbf45" stroke-width="3"/><line x1="16" y1="16" x2="44" y2="16" stroke="#6cbf45" stroke-width="3"/><circle cx="30" cy="32" r="5" fill="#6cbf45"/></svg>
  <h3>Nullam vulputate</h3>
  <p>Tellus eget nisl tincidunt fermentum. Aliquam ac ante quis lorem mattis rutrum at ut sem. Vivamus diam orci, condimentum.</p>
</div>
<div class="feature abs" style="left:790px;top:1310px">
  <svg width="60" height="60" viewBox="0 0 60 60" aria-hidden="true"><rect x="12" y="16" width="36" height="26" rx="3" fill="none" stroke="#6cbf45" stroke-width="3"/><line x1="18" y1="25" x2="32" y2="25" stroke="#6cbf45" stroke-width="3"/><line x1="18" y1="33" x2="28" y2="33" stroke="#6cbf45" stroke-width="3"/><circle cx="40" cy="29" r="4" fill="#6cbf45"/><line x1="20" y1="46" x2="40" y2="46" stroke="#6cbf45" stroke-width="3"/></svg>
  <h3>Nullam vulputate</h3>
  <p>Tellus eget nisl tincidunt fermentum. Aliquam ac ante quis lorem mattis rutrum at ut sem. Vivamus diam orci, condimentum.</p>
</div>

<div class="banner abs" role="img" aria-label="City skyline photograph washed in green"></div>
<h2 class="banner-title abs">Donec eget dui <span>tortor fusce</span> consequat</h2>
<p class="banner-text abs">In nulla quis blandit. Sed feugiat, lorem eu euismod laoreet, justo velit egestas sapien, vitae scelerisque sem sapien</p>
<span class="btn btn-outline abs">Learn more</span>
<span class="btn btn-solid abs">Start now</span>

<h2 class="section-title abs" style="top:2182px;color:var(--green)">Donec egetdui tortor fusce</h2>
<p class="section-lead abs" style="top:2228px;font-size:15px;line-height:25px">consequat in nulla quis blandit. Sed feugiat, lorem eu euismod laoreet, justo velit egestas sapien, vitae scelerisque sem sapien in risus</p>

<div class="tile abs" style="left:129px;background:linear-gradient(180deg,#4f82c6,#9fb7cf 60%,#5b6b78)" role="img" aria-label="Glass office building exterior"><div class="tile-label abs">Litora torquent<span>&rsaquo;</span></div></div>
<div class="tile abs" style="left:368px;background:linear-gradient(180deg,#8a8c8e,#3a4048 55%,#1d2228)" role="img" aria-label="Auditorium with rows of seats and a projection screen"><div class="tile-label abs">Litora torquent<span>&rsaquo;</span></div></div>
<div class="tile abs" style="left:604px;background:linear-gradient(180deg,#c9b48e,#6f5b43 55%,#d9cdb8)" role="img" aria-label="Living room with a wall mounted television"><div class="tile-label abs">Litora torquent<span>&rsaquo;</span></div></div>
<div class="tile abs" style="left:843px;background:linear-gradient(180deg,#2e2a26,#7a5a36 50%,#3a2c20)" role="img" aria-label="Bar with stools and hanging screens"><div class="tile-label abs">Litora torquent<span>&rsaquo;</span></div></div>

<div class="pricing abs"></div>
<div class="plan abs" style="left:129px"><div class="plan-ring"><small>Class</small><b>$250</b><em>Aptent Taciti</em></div><p>Donec eget tortor Fusce consequat in nulla quis blandit. Sed feugiat, lorem euismod laoreet, justo egestas sapien, scelerisquesapien in risus</p><span class="btn">Order</span></div>
<div class="plan abs" style="left:452px"><div class="plan-ring"><small>Class</small><b>$500</b><em>Aptent Taciti</em></div><p>Donec eget tortor Fusce consequat in nulla quis blandit. Sed feugiat, lorem euismod laoreet, justo egestas sapien, scelerisquesapien in risus</p><span class="btn">Order</span></div>
<div class="plan abs" style="left:775px"><div class="plan-ring"><small>Class</small><b>$750</b><em>Aptent Taciti</em></div><p>Donec eget tortor Fusce consequat in nulla quis blandit. Sed feugiat, lorem euismod laoreet, justo egestas sapien, scelerisquesapien in risus</p><span class="btn">Order</span></div>

<div class="partners abs"><span>Oakmill</span><span>Trellan</span><span>Wrenfield</span><span>Pellora</span><span>Mossline</span><span>Keystead</span></div>

<footer class="footer abs" role="img" aria-label="Faint world map behind the footer"></footer>
<div class="contact-card abs">
  <h4>Contact us</h4>
  <p>Donec interdum dapibus facilisis aliquam congue tempus augue non bibendum ipsum dictum</p>
  <div class="row"><h5><svg width="9" height="11" viewBox="0 0 9 11"><path d="M4.5 0a4 4 0 014 4c0 3-4 7-4 7s-4-4-4-7a4 4 0 014-4z" fill="#57a935"/></svg>Location</h5><p>240 Larkspur Row, Denholm</p></div>
  <div class="row"><h5><svg width="10" height="10" viewBox="0 0 10 10"><path d="M1 1l3 0 1 3-2 1c1 2 2 3 4 4l1-2 3 1 0 3C5 11-1 5 1 1z" fill="#57a935"/></svg>Phone</h5><p>(555) 014 2290</p></div>
  <div class="row"><h5><svg width="11" height="8" viewBox="0 0 11 8"><rect width="11" height="8" fill="#57a935"/><path d="M0 0l5.5 4L11 0" stroke="#fff" fill="none"/></svg>Email</h5><p>hello@brightfall.example</p></div>
</div>
<div class="map abs" role="img" aria-label="Street map showing the office location"></div>
<div class="comment abs">
  <h4>Leave a comment</h4>
  <div class="field">Your Name</div>
  <div class="field">Your Email</div>
  <div class="field tall">Message</div>
  <span class="btn">Submit</span>
</div>
<p class="copyright abs">Copyright &copy; by Brightfall Systems 2017. All right reserved.</p>

</body>
</html>
```